New Business Card Design Project

2 sided business card required. I have attached some previous designs of items we have had made so you can see the logo etc. we Want the card to look professional and modern. for the final design upload for winning designer please note I need to be able to edit the names / phone numbers on the card design as I need to get them made for different staff.
Updates

extending time so designers can have time to submit

Target Market(s)

new customers

Industry/Entity Type

transport / earthmoving

Contact Information for Business Card

name, phone number email address

Requirements
Nice to have
• professional / impressive looking card (first impressions to customers count)
Should not have
• do not put our mobile number on the design use a generic number

```html
<!DOCTYPE html>
<html lang="en">
<head>
<meta charset="utf-8">
<title>KRT Pty Ltd – Business Card</title>
<link href="https://fonts.googleapis.com/css2?family=Oswald:wght@500;600;700&family=Tinos:wght@700&display=swap" rel="stylesheet">
<style>
  :root {
    --backdrop: #3b3b3d;
    --card-black: #0b0b0b;
    --card-edge: #6b5532;
    --panel-dark: #1a1816;
    --panel-mid: #3a342c;
    --panel-bronze: #5a4c3b;
    --accent-orange: #d9923a;
    --text-white: #f4f4f4;
    --logo-tone: #b9a68c;
  }
  * { margin: 0; padding: 0; box-sizing: border-box; }
  html, body {
    width: 1200px; height: 1200px; overflow: hidden;
    background: var(--backdrop);
  }
  .canvas { position: relative; width: 1200px; height: 1200px; }

  .card {
    position: absolute; left: 150px;
    width: 900px; height: 514px;
    background: var(--card-black);
    border: 2px solid var(--card-edge);
    overflow: hidden;
  }
  .card--front { top: 60px; }
  .card--back  { top: 628px; }

  /* Front side */
  .front-photo {
    position: absolute; inset: 0;
    background:
      radial-gradient(ellipse at 60% 35%, var(--panel-bronze) 0%, var(--panel-mid) 30%, var(--panel-dark) 60%, var(--card-black) 90%);
  }
  .front-logo {
    position: absolute; left: 0; right: 0; top: 150px;
    text-align: center; white-space: nowrap;
    font-family: 'Oswald', sans-serif; font-weight: 600;
    font-size: 110px; letter-spacing: 4px;
    color: var(--logo-tone);
  }
  .front-email {
    position: absolute; left: 0; right: 0; top: 380px;
    display: flex; justify-content: center; align-items: center; gap: 18px;
    font-family: 'Tinos', serif; font-weight: 700; font-size: 26px;
    color: var(--text-white);
  }

  /* Back side */
  .back-graphics { position: absolute; inset: 0; }
  .back-logo {
    position: absolute; left: 560px; top: 80px; width: 340px;
    text-align: center; white-space: nowrap;
    font-family: 'Oswald', sans-serif; font-weight: 600;
    font-size: 56px; letter-spacing: 2px; line-height: 1.4;
    color: var(--logo-tone);
  }
  .contact {
    position: absolute; left: 50px; top: 22px;
  }
  .contact__name {
    font-family: 'Oswald', sans-serif; font-weight: 700;
    font-size: 54px; letter-spacing: 2px; line-height: 1;
    color: var(--accent-orange);
  }
  .contact__row {
    display: flex; align-items: center; gap: 16px; margin-top: 12px;
    color: var(--text-white);
  }
  .contact__phone {
    font-family: 'Oswald', sans-serif; font-weight: 600; font-size: 26px; letter-spacing: 2px;
  }
  .contact__email {
    font-family: 'Tinos', serif; font-weight: 700; font-size: 26px;
  }
  .services-title {
    position: absolute; left: 60px; top: 242px;
    font-family: 'Oswald', sans-serif; font-weight: 700;
    font-size: 34px; letter-spacing: 2px; line-height: 1.2;
    color: var(--text-white);
  }
  .service-list {
    position: absolute; list-style: none;
    font-family: 'Oswald', sans-serif; font-weight: 500;
    font-size: 17px; line-height: 1.6; letter-spacing: 0.5px;
    color: var(--accent-orange);
  }
  .service-list li { display: flex; align-items: center; gap: 14px; white-space: nowrap; }
  .service-list li::before {
    content: ""; width: 13px; height: 13px; flex: none;
    background: var(--text-white);
  }
  .service-list--one   { left: 36px;  top: 298px; }
  .service-list--two   { left: 325px; top: 352px; }
  .service-list--three { left: 625px; top: 392px; }
</style>
</head>
<body>
<div class="canvas">

  <!-- Front: company name side -->
  <section class="card card--front">
    <div class="front-photo" role="img" aria-label="Dark photograph of a road train under a metal mesh texture"></div>
    <div class="front-logo">KRT Pty Ltd</div>
    <div class="front-email">
      <svg width="26" height="18" viewBox="0 0 26 18" aria-hidden="true">
        <rect x="1" y="1" width="24" height="16" fill="none" stroke="#f4f4f4" stroke-width="2"/>
        <polyline points="1,1 13,10 25,1" fill="none" stroke="#f4f4f4" stroke-width="2"/>
      </svg>
      <span>xyz@haulmail.com</span>
    </div>
  </section>

  <!-- Back: contact and services side -->
  <section class="card card--back">
    <svg class="back-graphics" width="900" height="514" viewBox="0 0 900 514">
      <defs>
        <linearGradient id="lower-shade" x1="0" y1="0" x2="0" y2="1">
          <stop offset="0" stop-color="#1c1c1c"/>
          <stop offset="1" stop-color="#080808"/>
        </linearGradient>
        <radialGradient id="panel-tone" cx="0.6" cy="0.45" r="0.7">
          <stop offset="0" stop-color="#5a4c3b"/>
          <stop offset="0.45" stop-color="#2e2a25"/>
          <stop offset="1" stop-color="#121110"/>
        </radialGradient>
      </defs>
      <rect width="900" height="514" fill="#0b0b0b"/>
      <polygon points="0,185 900,315 900,514 0,514" fill="url(#lower-shade)"/>
      <polygon points="330,233 620,0 900,0 900,315" fill="url(#panel-tone)" role="img" aria-label="Photograph of a road train against a dark metal mesh"/>
      <line x1="0" y1="185" x2="900" y2="315" stroke="#f4f4f4" stroke-width="8"/>
      <line x1="330" y1="233" x2="620" y2="0" stroke="#f4f4f4" stroke-width="8"/>
    </svg>

    <div class="contact">
      <div class="contact__name">JOHN DOE</div>
      <div class="contact__row">
        <svg width="20" height="22" viewBox="0 0 20 22" aria-hidden="true">
          <path d="M4 1 L8 6 L6 9 Q9 14 13 16 L16 14 L19 18 L16 21 Q4 18 1 4 Z" fill="#f4f4f4"/>
        </svg>
        <span class="contact__phone">1234567890</span>
      </div>
      <div class="contact__row">
        <svg width="22" height="16" viewBox="0 0 22 16" aria-hidden="true">
          <rect x="1" y="1" width="20" height="14" fill="none" stroke="#f4f4f4" stroke-width="2"/>
          <polyline points="1,1 11,9 21,1" fill="none" stroke="#f4f4f4" stroke-width="2"/>
        </svg>
        <span class="contact__email">xyz@haulmail.com</span>
      </div>
    </div>

    <div class="back-logo">KRT Pty Ltd</div>

    <h2 class="services-title">OUR SERVICES</h2>
    <ul class="service-list service-list--one">
      <li>OVER SIZE LOADS | HOT SHOT LOADS</li>
      <li>HEAVY VEICHLE RECOVERY SERVICES</li>
      <li>POTABLE WATER DELIVERIES</li>
      <li>ROAD BUILDING/ MAINTAINENCE</li>
    </ul>
    <ul class="service-list service-list--two">
      <li>SAND METAL SUPPLY &amp; CARTAGE</li>
      <li>ROAD TRAIN TIPPERS</li>
      <li>ROAD TRAIN TANKERS</li>
      <li>ROAD TRAIN FLAT TOPS</li>
    </ul>
    <ul class="service-list service-list--three">
      <li>DROP DECK TRAILERS</li>
      <li>MINE SITE ACCREDITED</li>
      <li>EQUIPMENT &amp; OPERATA</li>
      <li>EARTHWORKS</li>
    </ul>
  </section>

</div>
</body>
</html>
```